Coffee label for grocery store sales

We need a 3x4 label designed for our expanding grocery store market. I'm looking for something playful that will be eye catching on a shelf. Bag color is negotiable, but would prefer kraft, white, or black.

Target Market(s)

Grocery Stores

Industry/Entity Type

Coffee Shop

Logo Text

Heron Lane Coffee

Colors

Designer to choose colors to be used in the design.

Requirements
Must have
• Space for address label to identify blend.
• 47 W. Oak Ave., Dunmore, WI 54921
• www.heronlanecoffee.example
Nice to have
• Illustrations, bold colors

```html
<!DOCTYPE html>
<html lang="en">
<head>
<meta charset="utf-8">
<title>Heron Lane Coffee – House Blend Label</title>
<link rel="stylesheet" href="https://fonts.googleapis.com/css2?family=Bebas+Neue&family=Allura&display=swap">
<style>
  :root {
    --kraft: #e4b98a;
    --mint: #d5ebe3;
    --roast: #7b4f2c;
    --tan: #d9a86a;
    --ink: #141414;
    --paper: #ffffff;
  }
  * { box-sizing: border-box; margin: 0; padding: 0; }
  html, body { width: 1200px; height: 896px; overflow: hidden; background: var(--kraft); }
  .label {
    position: absolute; left: 292px; top: 38px;
    width: 615px; height: 820px;
    background: var(--mint);
    overflow: hidden;
  }
  .hill { position: absolute; left: 0; top: 0; width: 615px; height: 820px; }
  .scene-art {
    position: absolute; left: 20px; top: 250px; width: 575px; height: 290px;
    border-radius: 8px;
    background: linear-gradient(180deg, rgba(213,235,227,0) 0%, #e2cba0 55%, #8a5c35 100%);
  }
  .brand {
    position: absolute; left: 125px; top: 26px;
    width: 365px; height: 205px;
    border: 6px solid var(--ink);
    border-radius: 12px;
    background: var(--mint);
    text-align: center;
    font-family: "Bebas Neue", sans-serif;
    font-weight: 400;
    color: var(--ink);
  }
  .brand-name {
    display: block; margin-top: 10px;
    font-size: 74px; line-height: 1; letter-spacing: 1px;
  }
  .brand-rule {
    display: block; margin: 34px 6px 0;
    height: 3px; background: var(--tan);
  }
  .brand-word {
    display: block; margin-top: 6px;
    font-size: 74px; line-height: 1; letter-spacing: 1px;
  }
  .address {
    position: absolute; left: 122px; right: 122px; top: 549px;
    padding: 4px 0 2px;
    border-top: 2px solid #3a2414; border-bottom: 2px solid #3a2414;
    text-align: center;
    font-family: "Bebas Neue", sans-serif;
    color: var(--tan);
    font-size: 26px; letter-spacing: 0.5px; line-height: 1;
  }
  .blend-panel {
    position: absolute; left: 20px; top: 604px; width: 574px; height: 190px;
    background: var(--paper);
    text-align: center;
  }
  .blend-name {
    display: block; margin-top: 26px;
    font-family: "Allura", cursive;
    font-size: 84px; line-height: 1; color: var(--ink);
  }
  .blend-origin {
    display: block; margin-top: 6px;
    font-family: "Bebas Neue", sans-serif;
    font-size: 36px; letter-spacing: 1px; color: var(--ink);
  }
  .website {
    position: absolute; left: 0; right: 0; top: 798px;
    text-align: center;
    font-family: "Bebas Neue", sans-serif;
    font-size: 17px; line-height: 1; letter-spacing: 1px;
    color: var(--tan);
  }
</style>
</head>
<body>
  <main class="label">
    <svg class="hill" viewBox="0 0 615 820" aria-hidden="true">
      <path d="M0 530 C150 480 330 440 615 455 L615 820 L0 820 Z" fill="var(--roast)"/>
    </svg>
    <div class="scene-art" role="img" aria-label="Illustration of a vintage truck loaded with coffee beans driving toward a coffee-grinder shaped shop on a brown hill under clouds"></div>
    <h1 class="brand">
      <span class="brand-name">Heron Lane</span>
      <span class="brand-rule"></span>
      <span class="brand-word">Coffee</span>
    </h1>
    <p class="address">47 W. Oak Ave., Dunmore, WI 54921</p>
    <section class="blend-panel">
      <span class="blend-name">House Blend</span>
      <span class="blend-origin">100% Arabica</span>
    </section>
    <p class="website">www.heronlanecoffee.example</p>
  </main>
</body>
</html>
```